One-Page Flat Design for SEO Company [2 DAYS]

We need a one-page flat design for our SEO company. Our current website is http://www.rankloft.com/. We are looking to completely re-design the site using new flat design techniques.
Below are some examples of the type of style we're going after:
http://quormel.com/
http://tobyrand.co.uk/
https://pentaly.co/
http://milesporter.me/
As you can see- flat, clean, minimal. It is very important you follow this type of style.
For colour scheme, you may use one of the pre-made colour palettes from here:
http://www.vornacle.com/blog/inspiration/24-flat-designs-with-compelling-color-palettes
I've attached a wireframe to be followed.
Hi,

```html
<!DOCTYPE html>
<html lang="en">
<head>
<meta charset="utf-8">
<title>RankLoft – SEO services that actually work</title>
<link rel="stylesheet" href="https://fonts.googleapis.com/css2?family=Open+Sans:wght@400&family=Arimo:wght@400;700&display=swap">
<style>
  :root {
    --nav-bg: #585858;
    --hero-bg: #98b482;
    --text-light: #ffffff;
    --brand-tint: #ffffff;
  }
  * { margin: 0; padding: 0; box-sizing: border-box; }
  html, body {
    width: 1200px;
    height: 540px;
    overflow: hidden;
    background: var(--hero-bg);
  }
  .page {
    position: relative;
    width: 1200px;
    height: 540px;
    overflow: hidden;
  }
  .site-header {
    height: 75px;
    background: var(--nav-bg);
    display: flex;
    align-items: center;
    justify-content: space-between;
    padding: 0 36px;
  }
  .brand {
    font-family: "Open Sans", sans-serif;
    font-weight: 400;
    font-size: 30px;
    letter-spacing: 0.5px;
    color: var(--brand-tint);
  }
  .main-nav ul {
    list-style: none;
    display: flex;
    gap: 40px;
  }
  .main-nav a {
    font-family: "Open Sans", sans-serif;
    font-size: 15px;
    color: var(--text-light);
    text-decoration: none;
  }
  .hero {
    text-align: center;
    color: var(--text-light);
  }
  .hero-title {
    font-family: "Arimo", sans-serif;
    font-weight: 700;
    font-size: 58px;
    line-height: 68px;
    margin-top: 105px;
  }
  .hero-lead {
    font-family: "Arimo", sans-serif;
    font-weight: 400;
    font-size: 29px;
    line-height: 34px;
    margin-top: 72px;
  }
</style>
</head>
<body>
<div class="page">
  <header class="site-header">
    <div class="brand">RANKLOFT</div>
    <nav class="main-nav">
      <ul>
        <li><a href="#home">HOME</a></li>
        <li><a href="#about">ABOUT</a></li>
        <li><a href="#work">WORK</a></li>
        <li><a href="#services">SERVICES</a></li>
        <li><a href="#team">TEAM</a></li>
        <li><a href="#contact">CONTACT</a></li>
      </ul>
    </nav>
  </header>
  <section class="hero" id="home">
    <h1 class="hero-title">Finally<br>SEO services that actually work.</h1>
    <p class="hero-lead">Top-notch SEO services that are guaranteed<br>to boost your search engine rankings.<br>100% Quendle friendly.</p>
  </section>
</div>
</body>
</html>
```